Design for Wordpress Theme for site like quillforge.de

Need a new professional Website design, for my wordpress theme
this theme: http://demobay.pexlorn.com/?theme=project
this should be like:
http://www.tul-brosk.de/
http://www.fennwirk.de/
http://www.taskvelm.com/
http://www.dienstkoral.de/
or something new modern design.
The design must be integrated in the wordpress theme .
The language of the site is in german, but the script/theme is multilingual and this should be stay.
The name of my site is bavlorn
The url of my site is bavlorn.de
Note please , it is about 8 pages to design, not only the Startpage
i.e.
- login Page
- User Menu page
- search page
- Project post page
Industry/Entity Type
It Professional
Number of Pages Required
5+ page
Look and feel
Each slider illustrates characteristics of the customer's brand and the style your logo design should communicate.

```html
<!DOCTYPE html>
<html lang="en">
<head>
<meta charset="utf-8">
<title>bavlorn – home</title>
<link href="https://fonts.googleapis.com/css2?family=Raleway:wght@300;400;500;600;700&family=Open+Sans:ital,wght@0,400;0,600;0,700;1,400&family=Arimo:wght@400;700&display=swap" rel="stylesheet">
<style>
:root{
  --blue:#00a9ec;
  --green:#4cc90a;
  --yellow:#f5b820;
  --dark:#222222;
  --text:#333333;
  --muted:#777777;
  --light:#f2f2f2;
  --white:#ffffff;
  --footer-text:#7d7d7d;
}
*{margin:0;padding:0;box-sizing:border-box}
html,body{width:1200px;height:2500px;overflow:hidden;background:var(--white)}
body{position:relative;font-family:"Arimo",Arial,sans-serif;color:var(--text)}
.abs{position:absolute}

/* header */
.site-header{position:absolute;left:0;top:0;width:1200px;height:100px;background:var(--blue)}
.brand{position:absolute;left:110px;top:18px;font-family:"Raleway",sans-serif;font-weight:300;font-size:46px;color:var(--white);letter-spacing:1px;text-transform:uppercase}
.call{position:absolute;left:730px;top:8px;font-family:"Raleway",sans-serif;font-size:24px;color:var(--white)}
.social-top{position:absolute;top:6px;width:28px;height:28px;border:2px solid var(--white);border-radius:50%}
.main-nav{position:absolute;top:70px;left:0;font-family:"Arimo",sans-serif;font-size:16px;color:var(--white)}
.main-nav span{position:absolute;white-space:nowrap}

/* hero */
.hero{position:absolute;left:0;top:100px;width:1200px;height:492px;background:linear-gradient(100deg,#d9d9d9 0%,#c4c4c4 35%,#8d8d8d 55%,#b9b6b2 75%,#e2e2e2 100%)}
.hero-card{position:absolute;left:100px;top:190px;width:382px;height:260px;background:var(--white);border-radius:4px;box-shadow:0 3px 10px rgba(0,0,0,.35)}
.hero-card h1{position:absolute;left:20px;top:16px;font-family:"Raleway",sans-serif;font-weight:400;font-size:30px;line-height:36px;color:var(--blue)}
.hero-card h1 strong{display:block;color:#444;font-weight:700;text-transform:uppercase}
.search-field{position:absolute;left:20px;top:112px;width:342px;height:55px;background:#e6e6e6;border:1px solid #cfcfcf;border-radius:4px;font-size:16px;color:#999;padding:17px 17px}
.btn{position:absolute;background:var(--green);color:var(--white);border-radius:3px;font-size:16px;text-align:center}
.hero-card .btn{top:192px;height:45px;line-height:45px}

/* features */
.features{position:absolute;left:0;top:592px;width:1200px;height:421px;background:var(--white)}
.feature-card{position:absolute;top:111px;width:305px;height:255px;border:1.5px solid var(--blue);text-align:center}
.feature-card h3{margin-top:44px;font-family:"Raleway",sans-serif;font-weight:400;font-size:25px;color:#444}
.feature-card p{margin:12px auto 0;width:260px;font-size:13px;line-height:20px;color:#888}
.feature-card .btn{left:90px;top:197px;width:125px;height:35px;line-height:35px;font-size:14px}
.feature-icon{position:absolute;top:45px;width:96px;height:96px;border-radius:50%;background:var(--white);border:3px solid var(--green)}
.slider-arrow{position:absolute;top:190px}

/* film */
.film{position:absolute;left:0;top:1013px;width:1200px;height:353px;background:var(--blue);color:var(--white)}
.film h2{position:absolute;left:98px;top:28px;width:590px;font-family:"Raleway",sans-serif;font-weight:700;font-size:28px;line-height:31px}
.film p{position:absolute;left:103px;width:560px;font-size:12.5px;line-height:18px}
.video-frame{position:absolute;left:697px;top:50px;width:390px;height:255px;background:var(--white);border-radius:6px;padding:8px}
.video-still{width:100%;height:100%;background:linear-gradient(135deg,#f7f7f7,#dcdcdc)}

/* benefits */
.benefits{position:absolute;left:0;top:1366px;width:1200px;height:402px;background:var(--light)}
.benefits h2{position:absolute;left:0;top:42px;width:1200px;text-align:center;font-family:"Raleway",sans-serif;font-weight:600;font-size:30px;color:#444}
.benefits h3{position:absolute;top:106px;font-family:"Raleway",sans-serif;font-weight:400;font-size:25px;color:var(--blue)}
.benefit-list{position:absolute;top:160px;list-style:none;font-family:"Open Sans",sans-serif;font-size:18px;color:#333}
.benefit-list li{height:40px;display:flex;align-items:flex-start;gap:12px}
.benefit-list svg{margin-top:5px;flex:none}

/* testimonials */
.testimonials{position:absolute;left:0;top:1768px;width:1200px;height:340px}
.testimonials h2{position:absolute;top:27px;width:1200px;text-align:center;font-family:"Raleway",sans-serif;font-weight:700;font-size:31px;color:#222}
.avatar{position:absolute;top:148px;width:102px;height:102px;border-radius:50%;border:3px solid #222;background:linear-gradient(160deg,#c9c9c9,#5b6472)}
.quote{position:absolute;top:157px;width:345px;font-family:"Open Sans",sans-serif;font-size:13.5px;line-height:18px;color:#666}
.quote cite{display:block;margin-top:6px;font-style:normal;font-weight:700;color:#222}
.divider{position:absolute;left:593px;top:155px;width:1px;height:90px;background:#ccc}

/* newsletter */
.newsletter-bar{position:absolute;left:125px;top:2108px;width:943px;height:47px;background:var(--green);border-radius:3px;overflow:hidden}
.newsletter-bar .icon-box{position:absolute;left:0;top:0;width:62px;height:47px;background:var(--yellow)}
.newsletter-bar .label{position:absolute;left:82px;top:14px;font-size:16px;color:var(--white)}
.newsletter-bar .field{position:absolute;left:615px;top:12px;width:223px;height:25px;background:var(--white);border-radius:10px}
.newsletter-bar .submit{position:absolute;left:848px;top:12px;width:77px;height:25px;background:var(--yellow);border-radius:4px;color:var(--white);font-size:12px;text-align:center;line-height:25px}

/* footer */
.site-footer{position:absolute;left:0;top:2180px;width:1200px;height:275px;background:var(--dark);color:var(--footer-text);font-family:"Raleway",sans-serif}
.site-footer h4{position:absolute;top:55px;font-weight:400;font-size:19px;color:var(--white)}
.site-footer .col{position:absolute;top:98px;font-size:13px;line-height:21px}
.site-footer .col b{color:var(--white);font-weight:700}
.site-footer .hl{color:var(--yellow)}
.foot-social{position:absolute;top:2396px;width:12px;height:12px;border-radius:50%;background:var(--white)}
.go-field{position:absolute;left:862px;top:2334px;width:170px;height:36px;background:#141414}
.go-btn{position:absolute;left:1037px;top:2334px;width:60px;height:36px;border:2px solid var(--yellow);color:var(--white);font-size:13px;text-align:center;line-height:32px;font-family:"Arimo",sans-serif}
.copyright{position:absolute;left:0;top:2455px;width:1200px;height:45px;background:var(--blue);color:var(--white);font-size:13px;text-align:center;line-height:45px}
</style>
</head>
<body>

<header class="site-header">
  <div class="brand">bavlorn</div>
  <div class="call">Call: 00-555-018-274</div>
  <span class="social-top" style="left:975px"></span>
  <span class="social-top" style="left:1023px"></span>
  <span class="social-top" style="left:1071px"></span>
  <nav class="main-nav">
    <span style="left:603px">Home</span>
    <span style="left:685px">About Us</span>
    <span style="left:798px">Why&nbsp; Bavlorn</span>
    <span style="left:935px">Services</span>
    <span style="left:1037px">Contact</span>
  </nav>
</header>

<section class="hero" role="img" aria-label="Photo of business professionals seated in a meeting"></section>
<div class="hero-card">
  <h1>Let's get the job done <strong>by professionals.</strong></h1>
  <div class="search-field">What Service do you need ?</div>
  <div class="btn" style="left:57px;width:168px">Add A New Project</div>
  <div class="btn" style="left:237px;width:125px">Try It. Free.</div>
</div>

<section class="features">
  <svg class="slider-arrow" style="left:26px" width="28" height="46" viewBox="0 0 28 46"><path d="M24 3 L5 23 L24 43" fill="none" stroke="#777" stroke-width="4"/></svg>
  <svg class="slider-arrow" style="left:1148px" width="28" height="46" viewBox="0 0 28 46"><path d="M4 3 L23 23 L4 43" fill="none" stroke="#777" stroke-width="4"/></svg>

  <div class="feature-card" style="left:99px">
    <h3>Natus &amp; Doloremque</h3>
    <p>Sed ut perspiciatis unde omnis iste natus error sit voluptatem accusantium dolorem­que laudantiu totam remeriam. Sed ut perspiciatis unde omnis iste natus error sit voluptatem accus</p>
    <div class="btn">Read more</div>
  </div>
  <div class="feature-card" style="left:441px">
    <h3>Natus &amp; Doloremque</h3>
    <p>Sed ut perspiciatis unde omnis iste natus error sit voluptatem accusantium dolorem­que laudantiu totam remeriam. Sed ut perspiciatis unde omnis iste natus error sit voluptatem accus</p>
    <div class="btn">Read more</div>
  </div>
  <div class="feature-card" style="left:794px">
    <h3>Natus &amp; Doloremque</h3>
    <p>Sed ut perspiciatis unde omnis iste natus error sit voluptatem accusantium dolorem­que laudantiu totam remeriam. Sed ut perspiciatis unde omnis iste natus error sit voluptatem accus</p>
    <div class="btn">Read more</div>
  </div>

  <div class="feature-icon" style="left:203px">
    <svg width="90" height="90" viewBox="0 0 90 90"><circle cx="45" cy="35" r="11" fill="#444"/><path d="M26 62 Q28 47 45 47 Q62 47 64 62 Z" fill="#444"/></svg>
  </div>
  <div class="feature-icon" style="left:545px">
    <svg width="90" height="90" viewBox="0 0 90 90"><rect x="27" y="32" width="36" height="26" rx="2" fill="none" stroke="#444" stroke-width="3.5"/><circle cx="37" cy="42" r="4" fill="#444"/><rect x="32" y="48" width="10" height="5" fill="#444"/><rect x="46" y="39" width="12" height="3" fill="#444"/><rect x="46" y="46" width="12" height="3" fill="#444"/></svg>
  </div>
  <div class="feature-icon" style="left:898px">
    <svg width="90" height="90" viewBox="0 0 90 90"><rect x="32" y="26" width="4" height="40" fill="#444"/><path d="M36 28 Q46 24 52 29 Q58 33 64 29 L64 48 Q58 52 52 48 Q46 43 36 47 Z" fill="#444"/></svg>
  </div>
</section>

<section class="film">
  <h2>simply explained A film for artisans who are looking for quick and easy jobs</h2>
  <p style="top:113px">There's a lot of noise on the internet and clutter when you search. How to get heard? How to get noticed? These are the challenges to marketing success.The Review of Online Trade &amp; Craft Marketing provides the latest thinking on how to achieve these objectives in this rapidly developing, new environment.</p>
  <p style="top:203px">The Review of Online Trade &amp; Craft Marketing is the major new peer-reviewed, professional journal for anyone involved in digital marketing. Authoritative, accurate and intellectually robust, it is written by the industry's top practitioners who will provide you with the compre­hensive, quality information you need to make your business grow online.</p>
  <div class="video-frame">
    <div class="video-still" role="img" aria-label="Explainer video still: sketched craftsmen around a website, with a hand pointing at the screen"></div>
    <svg class="abs" style="left:160px;top:95px" width="64" height="64" viewBox="0 0 64 64"><circle cx="32" cy="32" r="31" fill="#3a8fb0" opacity=".9"/><path d="M25 18 L47 32 L25 46 Z" fill="#fff"/></svg>
  </div>
</section>

<section class="benefits">
  <h2>Bavlorn is Germany's crafts website no. 1</h2>
  <h3 style="left:145px">Benefits for clients</h3>
  <h3 style="left:676px">Benefits for craftsmen</h3>
  <ul class="benefit-list" style="left:130px">
    <li><svg width="17" height="14" viewBox="0 0 17 14"><path d="M2 7 L6.5 11.5 L15 2" fill="none" stroke="#f5b820" stroke-width="3"/></svg>Quickly and easily include your order</li>
    <li><svg width="17" height="14" viewBox="0 0 17 14"><path d="M2 7 L6.5 11.5 L15 2" fill="none" stroke="#f5b820" stroke-width="3"/></svg>Decide who performs your order</li>
    <li><svg width="17" height="14" viewBox="0 0 17 14"><path d="M2 7 L6.5 11.5 L15 2" fill="none" stroke="#f5b820" stroke-width="3"/></svg>Find proven quality craftsmen</li>
    <li><svg width="17" height="14" viewBox="0 0 17 14"><path d="M2 7 L6.5 11.5 L15 2" fill="none" stroke="#f5b820" stroke-width="3"/></svg>Compare ratings of satisfied customers</li>
    <li><svg width="17" height="14" viewBox="0 0 17 14"><path d="M2 7 L6.5 11.5 L15 2" fill="none" stroke="#f5b820" stroke-width="3"/></svg>Contact artisans about their company profiles</li>
  </ul>
  <ul class="benefit-list" style="left:677px;top:154px">
    <li><svg width="17" height="14" viewBox="0 0 17 14"><path d="M2 7 L6.5 11.5 L15 2" fill="none" stroke="#f5b820" stroke-width="3"/></svg>Every month 50,000 new jobs waiting for you</li>
    <li><svg width="17" height="14" viewBox="0 0 17 14"><path d="M2 7 L6.5 11.5 L15 2" fill="none" stroke="#f5b820" stroke-width="3"/></svg>More than half a million visitors a month</li>
    <li><svg width="17" height="14" viewBox="0 0 17 14"><path d="M2 7 L6.5 11.5 L15 2" fill="none" stroke="#f5b820" stroke-width="3"/></svg>About 60% of our clients are homeowners</li>
    <li><svg width="17" height="14" viewBox="0 0 17 14"><path d="M2 7 L6.5 11.5 L15 2" fill="none" stroke="#f5b820" stroke-width="3"/></svg>Present your clients operating on the Internet</li>
    <li><svg width="17" height="14" viewBox="0 0 17 14"><path d="M2 7 L6.5 11.5 L15 2" fill="none" stroke="#f5b820" stroke-width="3"/></svg>Get Best Reviews for your work</li>
  </ul>
</section>

<section class="testimonials">
  <h2>Testimonials</h2>
  <div class="avatar" style="left:120px" role="img" aria-label="Portrait of client Oren Halsted"></div>
  <div class="quote" style="left:230px">"You are a legend. We have an audit in progress today and I was able to illustrate a "Live" recovery. Thank you for service above and beyond the call of duty. We really appreciate that."<cite>Oren Halsted, Corveth Planning</cite></div>
  <div class="divider"></div>
  <div class="avatar" style="left:630px" role="img" aria-label="Portrait of client Tomas Verrin"></div>
  <div class="quote" style="left:742px">"You are a legend. We have an audit in progress today and I was able to illustrate a "Live" recovery. Thank you for service above and beyond the call of duty. We really appreciate that."<cite>Tomas Verrin, Corveth Planning</cite></div>
</section>

<div class="newsletter-bar">
  <div class="icon-box">
    <svg class="abs" style="left:16px;top:12px" width="32" height="23" viewBox="0 0 32 23"><rect x="1" y="1" width="30" height="21" fill="#222"/><path d="M1 1 L16 13 L31 1" fill="none" stroke="#f5b820" stroke-width="2"/></svg>
  </div>
  <div class="label">Enter your email valid address to subscribe our Monthly Newsletter</div>
  <div class="field"></div>
  <div class="submit">Submit</div>
</div>

<footer class="site-footer">
  <h4 style="left:98px">About</h4>
  <h4 style="left:353px">Twitter Widget</h4>
  <h4 style="left:603px">Contact Info</h4>
  <h4 style="left:862px">Newsletter</h4>
  <div class="col" style="left:98px;width:240px">Lorem Ipsum is simply dummy text of the printing and typesetting industry. Lorem Ipsum has been the industry's standard dummy text ever since the 1500s, when an unknown printer took a galley.</div>
  <div class="col" style="left:355px;width:225px">
    <svg width="12" height="10" viewBox="0 0 12 10" style="margin-right:6px"><path d="M1 8 L11 2" stroke="#fff" stroke-width="2"/></svg>The Evolution Of Marla Quenby<br>
    <span class="hl" style="margin-left:24px">http://lnk.example/7TrwQa</span><br>
    <span style="margin-left:24px;font-size:11px">- Tuesday Mar 17 - 6:45am</span>
  </div>
  <div class="col" style="left:603px;width:240px">12 Lindenweg Strasse, Halvern 40217, DE<br><br><b>Phone:</b> +49 555 014 2287<br><b>Email:</b> &nbsp;<span class="hl">desk@bavlorn-theme.de</span></div>
  <div class="col" style="left:862px;width:240px">Please, subscribe to our latest news to be upafted.</div>
</footer>
<span class="foot-social" style="left:610px"></span>
<span class="foot-social" style="left:649px"></span>
<span class="foot-social" style="left:688px"></span>
<span class="foot-social" style="left:727px"></span>
<span class="foot-social" style="left:766px"></span>
<div class="go-field"></div>
<div class="go-btn">GO</div>
<div class="copyright">Copyright 2014-2015. ALL Rights reserved</div>

</body>
</html>
```